KLO Personal sucht Visitenkarten u. Briefpapier Design
It was a very good project! Very quick and perfect design!
Zielgruppe
Wir sind ein Liechtensteiner Personaldienstleisungsunternehmen welches sowohl in der klassischen Personalvermittlung als auch in der temporären Personalbereitstellung tätig ist. Unsere Branchen reichen von Baugewerbe, Handwerk, Gastro- und Hotelerie bis hin zu Produktion und Gesundheitswesen.
Achtung:
Habe gerade die files vom neuen Logo hochgeladen!!!
Aufgabenstellung
Visitienkarten designen.
Briefpapier Vorlagenerstellung.
Schlichtes Visitenkartendesign Business auf der nicht zuviele Informationen sind (das Wichtigste)
Vorderseite:
Logo (wird vor Abschluss noch in besserer Qualität hochgeladen)
Firmenname
Anschrift
Name
Funktion
Telefon
Fax
E-Mail
Homepage
Rückseite:
Kann Kreativ gestaltet werden, farblich (blau, gelb, schwarz, weiss), nach Möglichkeit keinen weissen Hintergrund.
!!Bitte keine Vorschläge mit dem Fotoscanner ... da! Danke.
Wir freuen uns auch auf kreative Vorschläge, welche etwas vom Briefing abweichen.
KLO - Team

```html
<!DOCTYPE html>
<html lang="de">
<head>
<meta charset="utf-8">
<title>KLO Personal – Briefpapier und Visitenkarten</title>
<link href="https://fonts.googleapis.com/css2?family=Source+Sans+3:wght@400;600;700&display=swap" rel="stylesheet">
<style>
  :root {
    --brand-blue: #1f4e9c;
    --brand-blue-dark: #163c80;
    --brand-yellow: #f2dc1c;
    --paper: #f1f0ef;
    --ink: #1d1d1d;
    --ink-soft: #555;
    --backdrop: #c9ccce;
    --font: "Source Sans 3", "Myriad Pro", Arial, sans-serif;
  }
  * { box-sizing: border-box; margin: 0; padding: 0; }
  html, body { width: 1200px; height: 900px; overflow: hidden; }
  body { background: var(--backdrop); font-family: var(--font); color: var(--ink); position: relative; }

  .wordmark { font-family: var(--font); font-weight: 700; color: var(--brand-blue); letter-spacing: .02em; white-space: nowrap; }

  /* Letterhead */
  .letterhead {
    position: absolute; left: 70px; top: 60px; width: 554px; height: 784px;
    background: var(--paper); box-shadow: 0 6px 18px rgba(0,0,0,.18);
  }
  .letterhead .wordmark { position: absolute; right: 50px; top: 48px; font-size: 28px; }
  .fold-mark { position: absolute; left: 0; width: 10px; height: 1px; background: #999; }
  .recipient { position: absolute; left: 60px; top: 178px; font-size: 8.5px; line-height: 1.35; }
  .recipient strong { font-weight: 700; }
  .recipient .zip { margin-top: 8px; }
  .letter-date { position: absolute; right: 50px; top: 232px; font-size: 8.5px; }
  .letter-body { position: absolute; left: 90px; right: 50px; top: 262px; font-size: 8.5px; line-height: 1.45; }
  .letter-body .subject { font-weight: 700; margin-bottom: 10px; }
  .letter-body p { margin-bottom: 9px; text-align: left; }
  .closing { position: absolute; left: 90px; top: 560px; font-size: 8.5px; line-height: 1.4; }
  .signature { width: 130px; height: 26px; margin: 4px 0 2px; border-radius: 4px;
    background: linear-gradient(90deg, rgba(70,60,140,.18), rgba(70,60,140,.05)); }
  .closing .role { font-size: 6.5px; color: var(--ink-soft); }

  .letter-footer {
    position: absolute; left: 0; right: 0; bottom: 0; height: 112px;
    background: var(--brand-blue); border-top: 3px solid var(--brand-yellow);
    color: #fff; font-size: 7px; line-height: 1.45;
    display: grid; grid-template-columns: 1.1fr 1fr 1fr 1.25fr; gap: 10px; padding: 26px 28px 0 60px;
  }
  .letter-footer strong { font-weight: 700; }
  .kv { display: grid; grid-template-columns: 42px auto; }

  /* Business cards */
  .card { position: absolute; width: 476px; height: 308px; box-shadow: 0 6px 18px rgba(0,0,0,.18); overflow: hidden; }
  .card-back { left: 672px; top: 90px; background: var(--brand-blue); }
  .card-back .pattern { position: absolute; inset: 0;
    background: linear-gradient(135deg, var(--brand-blue) 0%, var(--brand-blue-dark) 100%); }
  .card-back svg.accent { position: absolute; inset: 0; }
  .card-back .wordmark { position: absolute; left: 30px; bottom: 30px; color: #fff; font-size: 24px; }
  .card-back .web { position: absolute; right: 30px; bottom: 70px; color: #fff; font-size: 9px; }

  .card-front { left: 672px; top: 450px; background: var(--paper); }
  .card-front .wordmark { position: absolute; right: 28px; top: 26px; font-size: 26px; }
  .card-person { position: absolute; left: 30px; top: 128px; }
  .card-person .name { font-weight: 700; color: var(--brand-blue); font-size: 15px; }
  .card-person .role { font-size: 9px; color: var(--ink-soft); margin-bottom: 16px; }
  .card-contact { font-size: 9.5px; line-height: 1.5; }
  .card-contact .kv { grid-template-columns: 44px auto; }
  .card-contact.office { position: absolute; right: 28px; top: 92px; padding-left: 10px; border-left: 1px solid var(--brand-blue); }
  .card-band { position: absolute; left: 0; right: 0; bottom: 0; height: 38px; background: var(--brand-blue);
    border-top: 3px solid var(--brand-yellow); color: #fff; font-size: 9px; padding: 11px 30px; }
  .card-band strong { font-weight: 700; }
</style>
</head>
<body>

<section class="letterhead" aria-label="Briefpapier">
  <div class="wordmark">KLO Personal</div>
  <span class="fold-mark" style="top:262px"></span>
  <span class="fold-mark" style="top:524px"></span>

  <address class="recipient" style="font-style:normal">
    <strong>Beispielbau AG</strong><br>
    Anna Beispiel<br>
    Beispielstraße 10a
    <div class="zip">D - 012345 Musterstadt</div>
  </address>

  <div class="letter-date">Musterstadt, den 01.01.2013</div>

  <div class="letter-body">
    <div class="subject">Betreff: Irgendein Betrefftext wird dann hier stehen oder vielleicht auch nicht</div>
    <p>Sehr geehrte Damen und Herren,</p>
    <p>Lorem ipsum dolor sit amet, consectetur adipisicing elit, sed do eiusmod tempor incididunt ut labore et dolore magna aliqua. Ut enim ad minim veniam, quis nostrud exercitation ullamco laboris nisi ut aliquip ex ea commodo consequat. Duis aute irure dolor in reprehenderit in voluptate velit esse cillum dolore eu fugiat nulla pariatur. Excepteur sint occaecat cupidatat non proident, sunt in culpa qui officia deserunt mollit anim id est laborum.</p>
    <p>Bis nostrud exercitation ullam mmodo consequat. Duis aute in voluptate velit esse cillum dolore eu fugiat nulla pariatur. At vver eos et accusam dignissum qui blandit est praesent luptatum delenit aigue excepteur sint occae. Et harumd dereud facilis est er expedit distinct. Nam libe soluta nobis eligent optio est congue nihil impedit doming id quod maxim placeat facer possim omnis.</p>
    <p>Irure dolor in reprehend incididunt ut labore et dolore magna aliqua. Ut enim ad minim veniam, quis nostrud exercitation ullamco laboris nisi ut aliquip ex ea commodo consequat. Duis aute irure dolor in reprehenderit in voluptate velit esse molestaie cillum. Officia deserunt mollit anim id est laborum. Neque pecun modut est neque nonor et imper ned libidig met, consectetur adipiscing elit, sed ut labore et dolore magna aliquam.</p>
    <p>At vver eos et accusam dignissum qui blandit est praesent. Trenz pruca beynocguon doas nog apoply su trenz ucu hugh rasoluguon.</p>
  </div>

  <div class="closing">
    Mit freundlichen Grüßen
    <div class="signature" role="img" aria-label="Handschriftliche Unterschrift"></div>
    Lukas Berger<br>
    <span class="role">Geschäftsführer</span>
  </div>

  <footer class="letter-footer">
    <div><strong>KLO Anstalt</strong><br>Talstrasse 14<br>9499 Ruggell<br>Liechtenstein</div>
    <div class="kv"><span>Tel.:</span><span>+423 000 11 20</span><span>Fax:</span><span>+423 000 11 21</span><span>E-Mail:</span><span>office@klo.li</span><span>Web:</span><span>www.klo.li</span></div>
    <div class="kv"><span>Bank:</span><span>Landesbank</span><span>Inhaber:</span><span>Lukas Berger</span><span>BLZ:</span><span>000 000 00</span><span>KTO:</span><span>000 111 22</span></div>
    <div class="kv"><span>IBAN:</span><span>LI00 0000 0000 1111 2222 3</span><span>BIC:</span><span>XXXXLI22</span><span>Steuer-Nr.:</span><span>000 / 111 / 22222</span><span>Mobil:</span><span>+43 664 000 12 34</span></div>
  </footer>
</section>

<section class="card card-back" aria-label="Visitenkarte Rückseite">
  <div class="pattern" role="img" aria-label="Dekoratives Flächenmuster in Blautönen"></div>
  <svg class="accent" viewBox="0 0 476 308" aria-hidden="true">
    <line x1="0" y1="250" x2="476" y2="150" stroke="#f2dc1c" stroke-width="2.5"/>
  </svg>
  <div class="web">www.klo.li</div>
  <div class="wordmark">KLO Personal</div>
</section>

<section class="card card-front" aria-label="Visitenkarte Vorderseite">
  <div class="wordmark">KLO Personal</div>
  <div class="card-contact office">
    <div class="kv"><span>Tel.:</span><span>+423 000 11 20</span><span>Fax:</span><span>+423 000 11 21</span><span>E-Mail:</span><span>office@klo.li</span><span>Web:</span><span>www.klo.li</span></div>
  </div>
  <div class="card-person">
    <div class="name">Lukas Berger</div>
    <div class="role">Geschäftsführer</div>
    <div class="card-contact">
      <div class="kv"><span>Mobil:</span><span>+43 664 000 12 34</span><span>E-Mail:</span><span>lukas.berger@klo.li</span></div>
    </div>
  </div>
  <div class="card-band"><strong>KLO Anstalt</strong> | Talstrasse 14 | 9499 Ruggell | Liechtenstein</div>
</section>

</body>
</html>
```